Online trading school - Website design

We are building an online trading school (trading of shares, commodities, indices, currencies). The purpose is to teach online traders how to trade successfully. We need to design the homepage of the website and logo (bramwelloq.com will be the domain). The homepage will contain the following elements

- logo
- Sign in and Register links/buttons
- upper menu
- short introduction
- a couple of bullet points 'Why to join our school?'
- sign up form
- text
- bottom menu

Attached is a draft for the designer. The draft is just for an inspiration, the actual structure of the website can be different if the designer thinks so.

The designer is free to choose colors.

School

3 page

```html
<!DOCTYPE html>
<html lang="en">
<head>
<meta charset="utf-8">
<title>Bramwelloq – Online Trading School</title>
<link href="https://fonts.googleapis.com/css2?family=Lato:wght@300;400;700&family=Questrial&display=swap" rel="stylesheet">
<style>
:root{
  --blue:#1eade5;
  --blue-dark:#0e86c3;
  --ink:#151515;
  --text:#6a6a6a;
  --line:#e3e3e3;
  --soft:#f4f4f4;
  --white:#ffffff;
}
*{margin:0;padding:0;box-sizing:border-box}
html,body{width:746px;height:1200px;overflow:hidden;background:var(--white)}
body{position:relative;font-family:'Lato',sans-serif;color:var(--text)}
.abs{position:absolute}
.topbar{left:0;top:0;width:746px;height:31px;background:#f7f7f7;border-bottom:1px solid #ececec}
.hours{left:39px;top:10px;font-size:10px;color:#8a8a8a}
.social{right:36px;top:9px;display:flex;gap:12px}
.social span{width:12px;height:12px;border-radius:50%;background:#b5b5b5}
.logo{font-family:'Questrial',sans-serif;color:var(--ink);font-size:40px;letter-spacing:1px}
.login-field{top:46px;width:83px;height:23px;border:1px solid #d9d9d9;border-radius:2px;font-size:7px;color:#aaa;padding:7px 9px}
.login-btn{left:642px;top:46px;width:68px;height:23px;background:var(--ink);color:#fff;font-size:10px;text-align:center;line-height:23px;border-radius:2px}
.login-links{left:467px;top:79px;font-size:7px;color:#777;display:flex;gap:10px;align-items:center}
.box{width:7px;height:7px;border:1px solid #ccc;display:inline-block;margin-right:4px;vertical-align:-1px}
.nav{left:0;top:107px;width:746px;height:35px;background:var(--blue);display:flex}
.nav a{color:#fff;text-decoration:none;font-family:'Questrial',sans-serif;font-size:13px;line-height:35px;text-align:center;border-right:1px solid rgba(255,255,255,.25)}
.nav a.active{background:#1a1a1a}
.hero{left:0;top:142px;width:746px;height:306px;background:linear-gradient(100deg,#f8f9fb 0%,#eef1f5 45%,#e6e2e1 65%,#f2f4f7 100%)}
.signup{left:69px;top:191px;width:273px;height:207px;background:rgba(255,255,255,.8);border:1px solid #e6e8ea;padding:20px 31px}
.signup h2{font-family:'Questrial',sans-serif;font-weight:400;color:var(--blue);font-size:20px;margin-bottom:11px}
.field{width:211px;height:27px;border:1px solid #d6d6d6;background:#fff;margin-bottom:5px;font-size:8px;color:#aaa;padding:9px 14px}
.agree{font-size:8px;color:#666;margin:6px 0 0 4px}
.submit{margin:7px 0 0 153px;width:57px;height:18px;background:var(--blue);color:#fff;font-size:8px;text-align:center;line-height:18px}
.divider{left:0;width:746px;height:1px;background:#ececec}
h3{font-family:'Questrial',sans-serif;font-weight:400;color:var(--ink);font-size:20px}
.why{left:69px;top:500px}
.why ul{list-style:none;margin-top:16px}
.why li{font-size:13px;line-height:26.6px;color:var(--text);font-weight:300}
.why li::before{content:"";display:inline-block;width:4px;height:4px;background:var(--blue);margin-right:14px;vertical-align:3px}
.vline{left:333px;top:498px;width:1px;height:179px;background:#e2e2e2}
.intro{left:372px;top:500px;width:310px}
.intro h3 span{color:var(--blue)}
.intro p{margin-top:16px;font-size:13px;line-height:17.5px;font-weight:300}
.intro p small{font-size:11.5px}
.more{left:380px;top:642px;width:78px;height:23px;background:var(--blue);color:#fff;font-family:'Questrial',sans-serif;font-size:11px;text-align:center;line-height:23px}
.offer{left:0;top:733px;width:746px;height:232px;background:var(--soft);border-top:1px solid #ebebeb;padding:42px 69px 0}
.offer p{margin-top:14px;font-size:11.6px;line-height:15.4px;font-weight:300;color:#555}
.footer{left:0;top:965px;width:746px;height:191px;background:var(--blue);color:#fff}
.footer h4{font-family:'Questrial',sans-serif;font-weight:400;font-size:14px;margin-bottom:10px}
.col{top:30px;font-size:11px;line-height:15.2px;font-weight:300}
.email{width:141px;height:26px;background:rgba(255,255,255,.12);font-size:8px;padding:9px 14px}
.subscribe{margin:8px 0 0 87px;width:54px;height:21px;background:var(--ink);font-size:6.5px;text-align:center;line-height:21px;font-weight:700}
.flogo{font-family:'Questrial',sans-serif;font-size:26px;color:#fff;margin-bottom:4px}
.bottombar{left:0;top:1156px;width:746px;height:44px;background:var(--blue-dark);color:#fff;font-size:11px;padding:15px 41px;font-weight:300}
</style>
</head>
<body>
<div class="abs topbar"></div>
<div class="abs hours">Opening Hours: 9:00 AM - 8:30 PM</div>
<div class="abs social"><span></span><span></span><span></span></div>

<div class="abs logo" style="left:39px;top:44px">Bramwelloq</div>
<div class="abs login-field" style="left:467px">Username</div>
<div class="abs login-field" style="left:554px">*********</div>
<div class="abs login-btn">LOGIN</div>
<div class="abs login-links"><span><i class="box"></i>Remember Me</span><span>|</span><span>Signup</span><span>|</span><span>Forget password ?</span></div>

<nav class="abs nav">
  <a style="width:184px">About Our School</a>
  <a style="width:137px">Risk Warning</a>
  <a class="active" style="width:101px">FAQ</a>
  <a style="width:171px">Trading Glossary</a>
  <a style="width:153px;border:none">Contact Us</a>
</nav>

<div class="abs hero" role="img" aria-label="Hands typing on a white laptop keyboard"></div>
<form class="abs signup">
  <h2>Join our school now!</h2>
  <div class="field">First name</div>
  <div class="field">Last name</div>
  <div class="field">Email</div>
  <div class="agree"><i class="box"></i>Agree with our terms and conditions.</div>
  <div class="submit">SUBMIT</div>
</form>

<div class="abs divider" style="top:456px"></div>

<section class="abs why">
  <h3>Why to join us?</h3>
  <ul>
    <li>Best trading tips ever.</li>
    <li>Secret tips form experts.</li>
    <li>We teach how to trade online.</li>
    <li>Learn how to trade commodities.</li>
    <li>Learn now to become a trader.</li>
  </ul>
</section>
<div class="abs vline"></div>
<section class="abs intro">
  <h3>Introduction to <span>Bramwelloq</span></h3>
  <p>It is a long established fact that a reader will be distracted by the readable content of a page when looking at its layout. making it look like readable English.<small>The generated Lorem Ipsum is therefore always free from etc.</small></p>
</section>
<div class="abs more">READ MORE</div>

<section class="abs offer">
  <h3>What do we offer?</h3>
  <p>There are many variations of passages of Lorem Ipsum available, but the majority have suffered alteration in some form, by injected humour, or randomised words which don't look even slightly believable. If you are going to use a passage of Lorem Ipsum, you need to be sure there isn't anything embarrassing hidden in the middle of text. All the Lorem Ipsum generators on the Internet tend to repeat predefined chunks as necessary, making this the first true generator on the Internet. It uses a dictionary of over 200 Latin words, combined with a handful of model sentence structures, to generate Lorem Ipsum which looks reasonable. The generated Lorem Ipsum is therefore always free from repetition, injected humour, or non-characteristic words etc.</p>
</section>

<footer class="abs footer">
  <div class="abs col" style="left:39px"><h4>Quick Links</h4>About our School<br>Risk warning<br>FAQ<br>Trading Glossary<br>Contact Us</div>
  <div class="abs col" style="left:183px"><h4>Contact us</h4><b style="font-weight:700;font-size:12px">555-014-2290</b><br>212 Linden Row<br>Harrowgate, MA 01744</div>
  <div class="abs col" style="left:357px"><h4>Newsletter</h4><div class="email">Email Address</div><div class="subscribe">SUBSCRIBE</div></div>
  <div class="abs col" style="left:557px;top:28px;width:150px;font-size:10px;line-height:12.6px;font-weight:400"><div class="flogo">Bramwelloq</div>Lorem Ipsum is simply dummy text of the printing and typesetting industry, when an unknown printer took a galley of type e specimen book.</div>
</footer>
<div class="abs bottombar">Copyright 2016 Calder Mill group.All Rights Reserved.</div>
</body>
</html>
```